Business cards for financial advisor-insurance agent firm

Our company, Harlow Pemberton Insurance & Investments, is an insurance (health, life, home, auto, etc) and investment brokerage offering a suite of options to meet client needs. We need business cards that are professional and embody strength, security and sophistication.

Also running a letterhead project at
http://jobs.briefmarlo.com/job.aspx?id=519087

Target Market(s)

Upper middle class and wealthy

Industry/Entity Type

Investment

Requirements
Nice to have
• Looking for either white, navy blue, or gray cards

```html
<!DOCTYPE html>
<html lang="en">
<head>
<meta charset="utf-8">
<title>Harlow Pemberton – Business Cards</title>
<link rel="stylesheet" href="https://fonts.googleapis.com/css2?family=Cinzel:wght@400;500&family=Marcellus&family=Lato:wght@400;700&display=swap">
<style>
  :root {
    --navy: #3b4058;
    --ink: #2b3152;
    --slate: #66767f;
    --steel: #8fa3ad;
    --mist: #e3e6ec;
    --gray: #808083;
    --silver: #c6c6c6;
    --paper: #ffffff;
  }
  * { margin: 0; padding: 0; box-sizing: border-box; }
  html, body { width: 1200px; height: 1163px; overflow: hidden; background: var(--paper); }
  .sheet { position: relative; width: 1200px; height: 1163px; }

  .card { position: absolute; width: 284px; height: 493px; overflow: hidden; }
  .card--white { background: var(--paper); border: 2px solid var(--navy); }
  .card--navy { background: var(--navy); }
  .card--gray { background: var(--gray); }

  .front-1 { left: 47px; top: 52px; }
  .front-2 { left: 411px; top: 53px; }
  .front-3 { left: 803px; top: 53px; }
  .back-1 { left: 47px; top: 595px; }
  .back-2 { left: 415px; top: 596px; }
  .back-3 { left: 803px; top: 593px; }

  /* Front */
  .brand-mark {
    position: absolute; left: 0; right: 0; top: 66px;
    display: flex; justify-content: center; align-items: center; gap: 9px;
    font-family: "Cinzel", serif; font-size: 15px; font-weight: 500; letter-spacing: .5px;
  }
  .brand-mark .square { width: 14px; height: 14px; border: 2px solid currentColor; }

  .portrait {
    position: absolute; background: var(--paper);
    box-shadow: inset 14px 14px 10px -6px rgba(0,0,0,.38);
  }
  .front .portrait { left: 52px; top: 157px; width: 182px; height: 182px; }
  .card--white.front .portrait { left: 51px; top: 155px; }

  .company {
    position: absolute; left: 0; right: 0; top: 383px; text-align: center;
    font-family: "Cinzel", serif; font-size: 22px; font-weight: 500; line-height: 1;
    white-space: nowrap;
  }
  .company-sub {
    position: absolute; left: 0; right: 0; top: 408px; text-align: center;
    font-family: "Cinzel", serif; font-size: 11px; font-weight: 500; letter-spacing: .3px;
  }

  /* Back */
  .agent-name {
    position: absolute; left: 0; right: 0; top: 70px; text-align: center;
    font-family: "Marcellus", serif; font-size: 27px; font-weight: 400; line-height: 1; letter-spacing: 0;
    white-space: nowrap;
  }
  .agent-title {
    position: absolute; left: 0; right: 0; top: 98px; text-align: center;
    font-family: "Marcellus", serif; font-size: 16px; letter-spacing: .5px; line-height: 1.2;
  }
  .frame {
    position: absolute; left: 30px; top: 140px; width: 224px; height: 222px;
    border: 10px solid var(--slate); padding: 10px;
  }
  .frame .portrait { position: static; width: 100%; height: 100%; }
  .card--navy .frame { border-color: var(--slate); background: var(--ink); padding: 8px; }
  .card--gray .frame { border-color: var(--silver); border-width: 8px; background: var(--gray); padding: 10px; }

  .contact {
    position: absolute; left: 0; right: 0; top: 383px; text-align: center;
    font-family: "Lato", sans-serif; font-size: 13px; line-height: 27px; list-style: none;
    white-space: nowrap;
  }
  .contact b { font-weight: 700; }

  /* Colourways */
  .card--white .brand-mark, .card--white .company { color: var(--ink); }
  .card--white .company-sub { color: var(--slate); }
  .card--navy .brand-mark, .card--navy .company { color: var(--steel); }
  .card--navy .company-sub { color: var(--mist); }
  .card--gray .brand-mark, .card--gray .company { color: var(--ink); }
  .card--gray .company-sub { color: var(--silver); }

  .card--white .agent-name { color: var(--ink); }
  .card--white .agent-title { color: #7d95a2; }
  .card--navy .agent-name { color: var(--steel); }
  .card--navy .agent-title { color: var(--mist); }
  .card--gray .agent-name { color: var(--ink); }
  .card--gray .agent-title { color: var(--silver); }

  .card--white .contact { color: var(--ink); }
  .card--navy .contact { color: var(--mist); }
  .card--navy .contact .label { color: var(--steel); }
  .card--gray .contact { color: var(--ink); }
</style>
</head>
<body>
<main class="sheet">

  <section class="card card--white front front-1">
    <div class="brand-mark"><span class="square"></span>Harlow Pemberton</div>
    <div class="portrait" role="img" aria-label="Agent portrait photo"></div>
    <h1 class="company">Harlow Pemberton</h1>
    <p class="company-sub">Insurance &amp; Investments</p>
  </section>

  <section class="card card--navy front front-2">
    <div class="brand-mark"><span class="square"></span>Harlow Pemberton</div>
    <div class="portrait" role="img" aria-label="Agent portrait photo"></div>
    <h1 class="company">Harlow Pemberton</h1>
    <p class="company-sub">Insurance &amp; Investments</p>
  </section>

  <section class="card card--gray front front-3">
    <div class="brand-mark"><span class="square"></span>Harlow Pemberton</div>
    <div class="portrait" role="img" aria-label="Agent portrait photo"></div>
    <h1 class="company">Harlow Pemberton</h1>
    <p class="company-sub">Insurance &amp; Investments</p>
  </section>

  <section class="card card--white back back-1">
    <h2 class="agent-name">DANIEL ASHFORD</h2>
    <p class="agent-title">INSURANCE AGENT</p>
    <div class="frame"><div class="portrait" role="img" aria-label="Agent portrait photo"></div></div>
    <ul class="contact">
      <li><b class="label">Tel:</b> 555-0142</li>
      <li><b class="label">E-mail:</b> daniel@harlowpemberton.com</li>
      <li><b>www.harlowpemberton.com</b></li>
    </ul>
  </section>

  <section class="card card--navy back back-2">
    <h2 class="agent-name">DANIEL ASHFORD</h2>
    <p class="agent-title">INSURANCE AGENT</p>
    <div class="frame"><div class="portrait" role="img" aria-label="Agent portrait photo"></div></div>
    <ul class="contact">
      <li><b class="label">Tel:</b> 555-0142</li>
      <li><b class="label">E-mail:</b> daniel@harlowpemberton.com</li>
      <li><b>www.harlowpemberton.com</b></li>
    </ul>
  </section>

  <section class="card card--gray back back-3">
    <h2 class="agent-name">DANIEL ASHFORD</h2>
    <p class="agent-title">INSURANCE AGENT</p>
    <div class="frame"><div class="portrait" role="img" aria-label="Agent portrait photo"></div></div>
    <ul class="contact">
      <li><b class="label">Tel:</b> 555-0142</li>
      <li><b class="label">E-mail:</b> daniel@harlowpemberton.com</li>
      <li><b>www.harlowpemberton.com</b></li>
    </ul>
  </section>

</main>
</body>
</html>
```